BrindleFlow Van Wrap Design

We are home heating specialists. We fit boilers and central heating systems as well as servicing and repairing boilers in domestic properties. We have a new logo and need our vans design to undergo some modernisation. Our vans are Short wheel base carrow plus.
Website www.BrindleFlow.co.uk
Phone 01632 958274
List of work we do:
Central heating
Installation,
Servicing,
Repairs,
Target Market(s)
Home owners and landlords
Industry/Entity Type
Gas, central heating
Font styles to use
Other font styles liked:
- See logo fonts
Colors
0054AA
0677BA
7BADD7
CADEEF
E8F1F8
EE7325
F08F49
F5BC92
FAE3D3
FDF4ED
Requirements
Must have
- Phone number, logo, web address, Chatterly logo, fuel sound logo, Halden Kruse logo, list of work we do
Nice to have
- Warm design as we are heating specialists.
Should not have
- Too much blue. Our main colour is orange.

```html
<!DOCTYPE html>
<html lang="en">
<head>
<meta charset="utf-8">
<title>BrindleFlow Van Wrap Design</title>
<link href="https://fonts.googleapis.com/css2?family=Montserrat:wght@500;600&family=Arimo:wght@700&family=Roboto+Condensed:ital,wght@0,700;1,700&family=Tinos:ital@1&display=swap" rel="stylesheet">
<style>
  :root{
    --bg:#4a4a4a;
    --panel:#ffffff;
    --orange:#ee7325;
    --blue:#0054aa;
    --blue-mid:#0677ba;
    --blue-pale:#cadeef;
    --ink:#1a1a1a;
  }
  *{margin:0;padding:0;box-sizing:border-box}
  html,body{width:1101px;height:1200px;overflow:hidden;background:var(--bg)}
  .canvas{position:relative;width:1101px;height:1200px}

  .wrap-panel{position:absolute;left:50px;width:1000px;height:360px;background:var(--panel);border-radius:46px 46px 18px 18px;overflow:hidden}
  .wrap-panel--nearside{top:150px}
  .wrap-panel--offside{top:600px}
  .orange-band{position:absolute;left:0;right:0;bottom:0;height:48px;background:var(--orange)}

  .brand{position:absolute;display:flex;flex-direction:column;align-items:center}
  .brand__row{display:flex;align-items:center;gap:14px}
  .brand__dot{width:26px;height:26px;border-radius:50%;background:var(--orange)}
  .brand__name{font-family:"Montserrat",sans-serif;font-weight:500;font-size:62px;line-height:1;color:var(--orange)}
  .brand__tagline{margin-top:8px;font-family:"Montserrat",sans-serif;font-weight:600;font-size:11px;letter-spacing:6px;color:var(--blue)}

  .web{position:absolute;font-family:"Tinos",serif;font-style:italic;font-size:30px;letter-spacing:3px;color:var(--blue)}

  .services{position:absolute;list-style:none}
  .services li{height:28px;margin-bottom:9px;display:flex;align-items:center;background:var(--orange);color:#fff;font-family:"Arimo",sans-serif;font-weight:700;font-size:19px;white-space:nowrap}
  .services--right li{padding-left:12px;clip-path:polygon(0 0,100% 0,calc(100% - 26px) 100%,0 100%)}
  .services--left li{justify-content:flex-end;padding-right:14px;margin-left:auto;font-family:"Roboto Condensed",sans-serif;font-style:italic;clip-path:polygon(0 0,100% 0,100% 100%,20px 100%)}

  .phone{position:absolute;display:flex;align-items:center;gap:10px;font-family:"Arimo",sans-serif;font-weight:700;font-size:30px;color:var(--blue);white-space:nowrap}
  .phone--condensed{font-family:"Roboto Condensed",sans-serif}
  .social{position:absolute;display:flex;align-items:center;gap:12px;font-family:"Arimo",sans-serif;font-weight:700;font-size:13px;color:var(--blue);white-space:nowrap}
  .social__square{width:22px;height:22px;border-radius:4px;background:var(--blue-mid)}

  .partners{position:absolute;display:flex;align-items:center;gap:14px}
  .partners__badge{width:30px;height:30px;border-radius:4px;background:var(--blue-pale)}
  .partners__name{font-family:"Arimo",sans-serif;font-weight:700;font-size:13px;color:var(--blue);white-space:nowrap}

  .rear-panel{position:absolute;top:1010px;left:600px;width:450px;height:130px;background:var(--panel);border-radius:20px;overflow:hidden}
  .rear-web{position:absolute;left:0;right:0;top:34px;text-align:center;font-family:"Roboto Condensed",sans-serif;font-weight:700;font-size:34px;color:var(--orange)}
  .rear-panel .rear-bumper{position:absolute;left:0;right:0;bottom:0;height:30px;background:var(--ink)}
</style>
</head>
<body>
<main class="canvas">

  <section class="wrap-panel wrap-panel--nearside">
    <div class="brand" style="left:70px;top:120px">
      <div class="brand__row"><span class="brand__dot"></span><span class="brand__name">BrindleFlow</span></div>
      <span class="brand__tagline">YOUR HOME HEATING SPECIALISTS</span>
    </div>
    <div class="web" style="left:80px;top:225px">www.BrindleFlow.co.uk</div>
    <div class="partners" style="left:380px;top:268px">
      <span class="partners__badge" role="img" aria-label="fuel sound registration badge"></span>
      <span class="partners__name">Halden Kruse</span>
    </div>

    <ul class="services services--right" style="left:557px;top:48px">
      <li style="width:232px">CENTRAL HEATING</li>
      <li style="width:206px">INSTALLATION</li>
      <li style="width:180px">SERVICING</li>
      <li style="width:154px">REPAIRS</li>
    </ul>
    <div class="phone" style="left:580px;top:198px">
      <svg width="22" height="22" viewBox="0 0 22 22" aria-hidden="true"><rect width="22" height="22" rx="4" fill="#0677ba"/><path d="M5 9c0-3 12-3 12 0l-2 1-1-2H8l-1 2zM7 11h8l1 6H6z" fill="#fff"/></svg>
      01632 958274
    </div>
    <div class="social" style="left:580px;top:257px"><span class="social__square"></span>Chatterly · Brindle Heating LTD</div>

    <div class="orange-band"></div>
  </section>

  <section class="wrap-panel wrap-panel--offside">
    <ul class="services services--left" style="left:90px;top:48px;width:220px">
      <li style="width:220px">CENTRAL HEATING</li>
      <li style="width:196px">INSTALLATION</li>
      <li style="width:172px">SERVICING</li>
      <li style="width:148px">REPAIRS</li>
    </ul>
    <div class="phone phone--condensed" style="left:110px;top:200px">
      <svg width="22" height="22" viewBox="0 0 22 22" aria-hidden="true"><rect width="22" height="22" rx="4" fill="#0677ba"/><path d="M5 9c0-3 12-3 12 0l-2 1-1-2H8l-1 2zM7 11h8l1 6H6z" fill="#fff"/></svg>
      01632 958274
    </div>
    <div class="social" style="left:130px;top:262px"><span class="social__square"></span>Chatterly · Brindle Heating LTD</div>

    <div class="brand" style="left:450px;top:110px">
      <div class="brand__row"><span class="brand__dot"></span><span class="brand__name">BrindleFlow</span></div>
      <span class="brand__tagline">YOUR HOME HEATING SPECIALISTS</span>
    </div>
    <div class="web" style="left:470px;top:215px">www.BrindleFlow.co.uk</div>
    <div class="partners" style="left:500px;top:266px">
      <span class="partners__badge" role="img" aria-label="fuel sound registration badge"></span>
      <span class="partners__name">Halden Kruse</span>
    </div>

    <div class="orange-band"></div>
  </section>

  <section class="rear-panel">
    <div class="rear-web">www.BrindleFlow.co.uk</div>
    <div class="rear-bumper"></div>
  </section>

</main>
</body>
</html>
```